Birch Hollow Lodge & Harbour. A site that will sell our lifestyle and embody our vision.

We are after a fun interactive website for our property development.
Check out our ideas for layout and content.
Use stock videos and phots if we havent provide enough.
Ive attached our Logo.
We are easy to reach and work with. Love the crative process.1.Our Vision.. (This clicks through to vision page)
Nestled in the North East corner of Wenlow Lake , Sk amidst thousands of acres of natural beauty, a unique community is taking shape. A community that connectS people, nature and play. A place to find those simpler times.

2.Explore..(This clicks through to explore page)
Discover a new life of adventure, on the lake fishing, in the bush on our trail system or maybe the local golf course.

3. Live Here..(This through to Live page)
Birch Hollow has everything you need to start living a full life based in a thriving community.
Slow down and get to know nature and your neighbors

Target Market(s)

35-65 Lake Life

Coding

Coded - Design and coding required

Number of Pages Required

5+ page

Font styles to use
Other font styles liked:
• Anntonio

Colors
00AB8E
00BBA5
67D7C9
C6EFE9
E9F9F6
F0912C
F2A743
F7CA91
FBE8D2
FDF5EE

Requirements
Nice to have
• Interactive

```html
<!DOCTYPE html>
<html lang="en">
<head>
<meta charset="utf-8">
<title>Birch Hollow Lodge &amp; Harbour</title>
<link href="https://fonts.googleapis.com/css2?family=Bebas+Neue&family=Jost:wght@400;500&display=swap" rel="stylesheet">
<style>
:root{
  --ink:#ffffff;
  --page:#1b1b1b;
  --page-deep:#141414;
  --muted:#8a8a8a;
  --rule:rgba(255,255,255,.75);
  --dusk-top:#4a4136;
  --dusk-mid:#a4572a;
  --dusk-low:#5a3324;
  --sunset-sky:#3a2730;
  --sunset-glow:#b84a3c;
}
*{margin:0;padding:0;box-sizing:border-box}
html,body{width:1200px;height:3000px;overflow:hidden;background:var(--page)}
.canvas{position:relative;width:1200px;height:3000px;overflow:hidden;background:var(--page);color:var(--ink);font-family:"Jost",sans-serif}
.display{font-family:"Bebas Neue",sans-serif;font-weight:400}
.abs{position:absolute}

/* hero */
.hero{left:0;top:0;width:1200px;height:656px;
  background:radial-gradient(ellipse 520px 300px at 600px 330px,#b9682d 0%,#8a4a26 45%,rgba(40,32,26,0) 100%),
  linear-gradient(180deg,var(--dusk-top) 0%,#7a5236 35%,var(--dusk-mid) 50%,var(--dusk-low) 70%,#2a2520 100%)}
.hero-scrim{left:0;top:0;width:1200px;height:656px;
  background:linear-gradient(90deg,rgba(20,22,18,.9) 0%,rgba(20,22,18,0) 28%,rgba(20,22,18,0) 72%,rgba(20,22,18,.9) 100%)}
.menu{left:86px;top:46px;display:flex;align-items:center;gap:6px;font-size:26px;letter-spacing:3px}
.menu svg{display:block}
.brand{left:500px;top:108px;width:200px;text-align:center;font-size:26px;letter-spacing:1px;line-height:1}
.brand small{display:block;font-size:10px;letter-spacing:2px;margin-top:4px}
.btn-outline{border:2px solid var(--ink);display:flex;align-items:center;justify-content:center;font-family:"Bebas Neue",sans-serif;font-size:22px;letter-spacing:6px;color:var(--ink)}
.contact-top{left:949px;top:36px;width:166px;height:51px}
.kicker{left:0;top:208px;width:1200px;text-align:center;font-size:34px;letter-spacing:30px;padding-left:30px}
.hero-title{left:0;top:248px;width:1200px;text-align:center;font-size:150px;letter-spacing:28px;padding-left:28px;line-height:1}
.scroll{left:545px;top:528px}
.progress{left:0;top:652px;width:1200px;height:6px;background:#555}
.progress span{display:block;width:184px;height:6px;background:var(--ink)}

/* feature rows */
.feature-title{font-size:50px;letter-spacing:20px;line-height:1}
.feature-copy{border-left:1px solid var(--rule);padding-left:26px;font-size:17px;line-height:30px}
.know-more{width:197px;height:52px;font-size:18px;letter-spacing:5px;gap:6px}
.photo{border-radius:50%}
.photo-vision{left:640px;top:740px;width:490px;height:440px;
  background:radial-gradient(ellipse at 50% 45%,#9aa3ae 0%,#6f7a5a 40%,#3a4434 62%,rgba(27,27,27,0) 72%)}
.photo-explore{left:80px;top:1260px;width:490px;height:470px;
  background:radial-gradient(ellipse at 50% 50%,#c9c9c6 0%,#8d8e86 38%,#3d4636 60%,rgba(27,27,27,0) 72%)}
.photo-live{left:620px;top:1790px;width:520px;height:470px;
  background:radial-gradient(ellipse at 50% 50%,#8e9cb8 0%,#6a6f88 35%,#6a3a3a 52%,rgba(27,27,27,0) 72%)}

/* closing band */
.closing{left:0;top:2320px;width:1200px;height:680px;
  background:linear-gradient(180deg,var(--page) 0%,var(--sunset-sky) 22%,#6c3540 42%,var(--sunset-glow) 62%,#3a1c1c 80%,#151313 100%)}
.closing-trees{left:0;top:2560px;width:1200px;height:440px;
  background:linear-gradient(180deg,rgba(18,16,16,0) 0%,rgba(18,16,16,.75) 45%,#161414 100%)}
.closing-kicker{left:0;top:2480px;width:1200px;text-align:center;font-size:22px;letter-spacing:4px}
.closing-title{left:0;top:2518px;width:1200px;text-align:center;font-size:116px;letter-spacing:10px;line-height:1}

/* footer */
.footer-brand{left:86px;top:2922px;font-size:34px;letter-spacing:2px;line-height:1}
.footer-brand small{display:block;font-size:12px;letter-spacing:3px;margin-top:4px}
.social{left:524px;top:2848px;display:flex;gap:8px}
.social a{width:45px;height:50px;border:2px solid var(--ink);display:flex;align-items:center;justify-content:center;font-family:"Bebas Neue",sans-serif;font-size:16px;letter-spacing:1px;color:var(--ink);text-decoration:none}
.contact-bottom{left:949px;top:2848px;width:166px;height:51px}
.legal{left:0;top:2934px;width:1200px;text-align:center;font-size:14px;line-height:24px;color:var(--muted)}
.legal strong{color:var(--ink);font-weight:500}
</style>
</head>
<body>
<main class="canvas">

  <section>
    <div class="abs hero" role="img" aria-label="Sunset over a calm lake framed by silhouetted pine branches"></div>
    <div class="abs hero-scrim"></div>

    <div class="abs menu display">
      <svg width="22" height="16" viewBox="0 0 22 16"><path d="M0 2h22M0 8h15M0 14h9" stroke="#fff" stroke-width="2"/></svg>
      MENU
    </div>
    <div class="abs brand display">BIRCH HOLLOW<small>LODGE &amp; HARBOUR</small></div>
    <a class="abs btn-outline contact-top">CONTACT</a>

    <p class="abs kicker display">CONNECT TO</p>
    <h1 class="abs hero-title display">NATURE</h1>

    <svg class="abs scroll" width="110" height="110" viewBox="0 0 110 110" aria-label="Scroll down">
      <defs><path id="ring" d="M55 55 m-42 0 a42 42 0 1 1 84 0 a42 42 0 1 1 -84 0"/></defs>
      <text fill="#fff" font-family="Jost,sans-serif" font-size="14" letter-spacing="9"><textPath href="#ring" startOffset="4%">SCROLL DOWN •</textPath></text>
      <path d="M55 38v34M49 66l6 6 6-6" stroke="#fff" stroke-width="1.5" fill="none"/>
    </svg>

    <div class="abs progress"><span></span></div>
  </section>

  <section>
    <h2 class="abs feature-title display" style="left:86px;top:790px">OUR VISION</h2>
    <p class="abs feature-copy" style="left:86px;top:866px;width:500px">Nestled in the North East corner of Wenlow Lake , Sk amidst thousands of acres of natural beauty, a unique community is taking shape. A community that connectS people, nature and play. A place to find those simpler times.</p>
    <a class="abs btn-outline know-more" style="left:86px;top:1027px">KNOW MORE <svg width="20" height="10" viewBox="0 0 20 10"><path d="M0 5h18M14 1l4 4-4 4" stroke="#fff" stroke-width="1.5" fill="none"/></svg></a>
    <div class="abs photo photo-vision" role="img" aria-label="Lakeside home on a green shore reflected in still water under a cloudy sky"></div>

    <div class="abs photo photo-explore" role="img" aria-label="Bald eagle perched on rocks by the lake, framed by branches"></div>
    <h2 class="abs feature-title display" style="left:601px;top:1343px">EXPLORE</h2>
    <p class="abs feature-copy" style="left:601px;top:1418px;width:510px">Discover&nbsp; a new life of adventure, on the lake fishing, in the bush on our trail system or maybe the local golf course.</p>
    <a class="abs btn-outline know-more" style="left:602px;top:1519px">KNOW MORE <svg width="20" height="10" viewBox="0 0 20 10"><path d="M0 5h18M14 1l4 4-4 4" stroke="#fff" stroke-width="1.5" fill="none"/></svg></a>

    <h2 class="abs feature-title display" style="left:86px;top:1925px">LIVE HERE</h2>
    <p class="abs feature-copy" style="left:86px;top:2001px;width:510px">Birch Hollow has everything you need to start living a full life based in a thriving community.</p>
    <a class="abs btn-outline know-more" style="left:86px;top:2091px">KNOW MORE <svg width="20" height="10" viewBox="0 0 20 10"><path d="M0 5h18M14 1l4 4-4 4" stroke="#fff" stroke-width="1.5" fill="none"/></svg></a>
    <div class="abs photo photo-live" role="img" aria-label="Person standing at the end of a red dock in morning fog"></div>
  </section>

  <section>
    <div class="abs closing" role="img" aria-label="Pink and red sunset sky behind a line of spruce tree silhouettes"></div>
    <div class="abs closing-trees"></div>
    <p class="abs closing-kicker display">BIRCH HOLLOW HAS EVERYTHING YOU NEED TO START LIVING A FULL LIFE BASED IN A</p>
    <h2 class="abs closing-title display">THRIVING COMMUNITY</h2>
  </section>

  <footer>
    <div class="abs footer-brand display">BIRCH HOLLOW<small>LODGE &amp; HARBOUR</small></div>
    <nav class="abs social">
      <a>FERN</a><a>LOON</a><a>REED</a>
    </nav>
    <a class="abs btn-outline contact-bottom">CONTACT</a>
    <p class="abs legal">© 2023 <strong>Birch Hollow Lodge &amp; Harbour</strong>. All right reserved<br>November 24,2023. Layout_4</p>
  </footer>

</main>
</body>
</html>
```